Bodywork Quietude Business Card Design

I want to create a very elegant and sophisticated two sided business card for my massage practice (www.bodyworkquietude.net). I have attached the logo and a PDF with some ideas down for the back of the card but I am open to suggestions. I will want to tie in a post card and flyer to the card later.
Similar colors to website would be great.
Target Market(s)
High end clientele, people looking for a sophisticated spa experience.
Industry/Entity Type
Massage
Contact Information for Business Card
Bodywork Quietude
7318 Larkspur Ave S, Suite 305
Seattle, WA 98103
(206) 555-0147
www.bodyworkquietude.net
Look and feel

```html
<!DOCTYPE html>
<html lang="en">
<head>
<meta charset="utf-8">
<title>Bodywork Quietude – Business Card</title>
<link href="https://fonts.googleapis.com/css2?family=Open+Sans:ital,wght@0,400;0,600;1,700&family=Tinos:wght@400&display=swap" rel="stylesheet">
<style>
  :root{
    --navy:#1d3e55;
    --navy-deep:#15303f;
    --cream:#f3efe6;
    --cream-deep:#e6dfd1;
    --ink:#222a30;
    --white:#ffffff;
    --stage:#e4e4e6;
  }
  *{box-sizing:border-box;margin:0;padding:0}
  html,body{width:1200px;height:1200px;overflow:hidden;background:var(--stage)}
  body{position:relative;font-family:"Open Sans",sans-serif}

  .card{position:absolute;left:170px;width:860px;height:491px;border-radius:4px;overflow:hidden;
        box-shadow:0 14px 30px rgba(0,0,0,.18)}
  .card--front{top:75px;background:linear-gradient(135deg,var(--cream) 0%,var(--cream-deep) 100%)}
  .card--back{top:630px;background:radial-gradient(ellipse at 40% 30%,#26506b 0%,var(--navy) 45%,var(--navy-deep) 100%);color:var(--white)}

  .decor{position:absolute;border-radius:50%}
  .card--front .decor{left:-60px;top:-40px;width:520px;height:520px;
        background:radial-gradient(circle,rgba(200,190,170,.18) 0%,rgba(200,190,170,0) 70%)}
  .card--back .decor{right:-80px;bottom:-90px;width:420px;height:420px;
        background:radial-gradient(circle,rgba(120,160,185,.16) 0%,rgba(120,160,185,0) 70%)}

  .name-band{position:absolute;left:0;top:60px;width:520px;height:128px;background:var(--navy);
        border-radius:0 64px 64px 0;color:var(--white);padding:20px 0 0 56px}
  .name-band__name{font-family:"Tinos",serif;font-size:50px;line-height:1.1}
  .name-band__title{font-size:22px;margin-top:4px}

  .contact{position:absolute;left:56px;top:232px;list-style:none;font-size:23px;color:var(--ink);line-height:1.4}
  .contact li{display:flex;align-items:flex-start;gap:12px}
  .contact svg{width:20px;height:20px;flex:none;margin-top:6px;fill:var(--navy)}
  .contact .indent{padding-left:32px}

  .brand{display:flex;align-items:center;gap:14px;font-family:"Tinos",serif;color:var(--navy);letter-spacing:1px}
  .brand__dot{border-radius:50%;background:var(--navy);flex:none}
  .card--front .brand{position:absolute;right:40px;top:270px;width:210px;flex-direction:column;
        text-align:center;font-size:32px;line-height:1.15;gap:12px}
  .card--front .brand__dot{width:60px;height:60px}
  .card--back .brand{justify-content:center;color:var(--white);font-size:30px;margin-top:34px}
  .card--back .brand__dot{width:40px;height:40px;background:var(--white)}

  .back__inner{position:relative;text-align:center}
  .headline{font-weight:700;font-style:italic;font-size:29px;line-height:1.3;margin:22px 60px 0}
  .specialties{display:inline-block;border:2px solid var(--white);padding:4px 18px;font-size:24px;margin-top:20px}
  .services{list-style:none;font-size:24px;margin-top:14px;line-height:1.4}
  .services li::before{content:"•";margin-right:8px}
</style>
</head>
<body>

<section class="card card--front" aria-label="Card front">
  <div class="decor" role="img" aria-label="Faint floral ornament in cream tones"></div>
  <div class="name-band">
    <div class="name-band__name">Daniel Whitford</div>
    <div class="name-band__title">Managing Director</div>
  </div>
  <ul class="contact">
    <li><svg viewBox="0 0 20 20"><path d="M4 2h4l2 5-2.5 1.5a11 11 0 0 0 4 4L13 10l5 2v4a2 2 0 0 1-2 2A15 15 0 0 1 2 4a2 2 0 0 1 2-2z"/></svg>(206) 555-0147</li>
    <li><svg viewBox="0 0 20 20"><path d="M2 5h16v10H2z M2 5l8 6 8-6" fill="none" stroke="#1d3e55" stroke-width="2"/></svg>Dan@BodyworkQuietude.net</li>
    <li><svg viewBox="0 0 20 20"><circle cx="10" cy="10" r="8" fill="none" stroke="#1d3e55" stroke-width="2"/><path d="M2 10h16M10 2c-4 5-4 11 0 16M10 2c4 5 4 11 0 16" fill="none" stroke="#1d3e55" stroke-width="1.5"/></svg>www.bodyworkquietude.net</li>
    <li><svg viewBox="0 0 20 20"><path d="M10 2l8 7h-2v8h-4v-5H8v5H4V9H2z"/></svg>7318 Larkspur Ave S, Suite 305</li>
    <li class="indent">Seattle, WA 98103</li>
  </ul>
  <div class="brand"><span class="brand__dot"></span><span>BODYWORK<br>QUIETUDE</span></div>
</section>

<section class="card card--back" aria-label="Card back">
  <div class="decor" role="img" aria-label="Faint floral ornament in blue tones"></div>
  <div class="back__inner">
    <div class="brand"><span class="brand__dot"></span>BODYWORK QUIETUDE</div>
    <p class="headline">Come and Experience the Most Relaxing and Invitingly Deep Massage of Your Life.....</p>
    <div class="specialties">Our Specialties</div>
    <ul class="services">
      <li>Deep Lomi Ultra Relaxation Massage</li>
      <li>Nurturing Touch Massage</li>
      <li>Hot Yoga Massage</li>
    </ul>
  </div>
</section>

</body>
</html>
```